1/2 Page add for BRMTL Conference

We are looking for a 1/2 page ad to support the annual BRMTL conference. I want to encourage the attendees to come to our both so we can explain how they can save money on food and supplies. here is a link to the conference. https://www.brmtl-example.org/conference/ here is our website www.pantrywisehub-example.com - the what we do can be captured in the ad. We will be at booth 505. Our goal is to get people to our booth #212 to explain the services that we provide –

Discounted food pricing
Free menu planning/design
Use of Registered Dietitian
Huge selection of discounted PPE and other necessary supplies to run any child care center

We have over 6000 members in 46 States and work with both small and large food distributors. We have been a sponsor of the association for the last 10 years.

Target Market(s)

Child care centers

Requirements
Must have
• Booth number -outline of what we do --- Stress we are a FREE service getting our members reduced pricing on food and supplies

```html
<!DOCTYPE html>
<html lang="en">
<head>
<meta charset="utf-8">
<title>PantryWise Hub – Half Page Ad</title>
<link rel="stylesheet" href="https://fonts.googleapis.com/css2?family=Montserrat:wght@500;700;800&family=Roboto+Condensed:wght@400;500&display=swap">
<style>
  :root{
    --navy:#0b4d8c;
    --green:#62ad57;
    --green-light:#9bd08d;
    --sky:#3f86cc;
    --ink:#474747;
    --paper:#ffffff;
    --paper-shade:#eceeef;
    --stage:#d6d6d6;
    --white:#ffffff;
  }
  *{margin:0;padding:0;box-sizing:border-box}
  html,body{width:1200px;height:1200px;overflow:hidden;background:var(--stage)}
  .ad{
    position:absolute;left:40px;top:220px;width:1120px;height:759px;overflow:hidden;
    background:linear-gradient(135deg,var(--paper) 0%,var(--paper-shade) 55%,var(--paper) 100%);
    font-family:"Montserrat",sans-serif;
  }
  .ad-art{position:absolute;inset:0}
  .brand{position:absolute;left:54px;top:58px;display:flex;align-items:center;gap:18px}
  .brand-square{width:46px;height:46px;background:var(--green)}
  .brand-name{font-weight:500;font-size:44px;color:var(--ink);letter-spacing:-1px;line-height:1}
  .headline{position:absolute;left:56px;top:210px;transform:rotate(-5deg);transform-origin:left top;font-weight:800;line-height:.92}
  .headline-lead{font-size:44px;color:var(--ink);display:block}
  .headline-food{font-size:84px;color:var(--green);display:block;margin-top:14px}
  .headline-supplies{font-size:84px;color:var(--navy);display:block}
  .services-ribbon{
    position:absolute;left:62px;top:476px;width:404px;height:40px;transform:rotate(-6deg);
    background:var(--green-light);border:3px solid var(--navy);
    clip-path:polygon(0 0,100% 0,96% 50%,100% 100%,0 100%,4% 50%);
    display:flex;align-items:center;justify-content:center;
    font-weight:800;font-size:24px;color:var(--navy);
  }
  .services{position:absolute;font-family:"Roboto Condensed",sans-serif;color:var(--white);font-size:19px;list-style:none;transform:rotate(-5deg);transform-origin:left top;line-height:35px}
  .services li{position:relative;padding-left:28px}
  .services li::before{content:"";position:absolute;left:2px;top:10px;width:14px;height:8px;border-left:4px solid var(--green-light);border-bottom:4px solid var(--green-light);transform:rotate(-45deg)}
  .services-left{left:33px;top:548px}
  .services-right{left:284px;top:518px;line-height:27px;white-space:nowrap}
  .cta{position:absolute;left:44px;top:660px;transform:rotate(-5deg);transform-origin:left top;font-weight:800;color:var(--white);line-height:1.2}
  .cta-request{font-size:28px;display:block}
  .cta-free{color:var(--green-light)}
  .cta-call{font-size:32px;display:block;margin-left:70px}
  .website{position:absolute;left:618px;top:716px;transform:rotate(-6deg);transform-origin:left top;display:flex;align-items:center;gap:10px;color:var(--white);font-weight:800;font-size:21px;white-space:nowrap}
  .booth{position:absolute;left:866px;top:730px;transform:rotate(-5deg);transform-origin:left top;color:var(--white);font-weight:800;font-size:18px}
</style>
</head>
<body>
<div class="ad">
  <svg class="ad-art" viewBox="0 0 1120 759" width="1120" height="759">
    <defs>
      <linearGradient id="bandGrad" x1="0" x2="1" y1="0" y2="0">
        <stop offset="0" stop-color="#0b4d8c"/><stop offset=".55" stop-color="#0b4d8c"/><stop offset="1" stop-color="#243447"/>
      </linearGradient>
      <linearGradient id="photoPeople" x1="0" x2="1"><stop offset="0" stop-color="#3c5a6b"/><stop offset="1" stop-color="#8a6a58"/></linearGradient>
      <linearGradient id="photoKids" x1="0" x2="1"><stop offset="0" stop-color="#5b8a4a"/><stop offset="1" stop-color="#c9a58a"/></linearGradient>
      <linearGradient id="photoProduce" x1="0" x2="1" y1="0" y2="1"><stop offset="0" stop-color="#d9dcd2"/><stop offset=".6" stop-color="#d86b3a"/><stop offset="1" stop-color="#6f9c4a"/></linearGradient>
      <linearGradient id="photoPpe" x1="0" x2="1"><stop offset="0" stop-color="#e9cf8f"/><stop offset="1" stop-color="#9fb0cf"/></linearGradient>
    </defs>
    <polygon class="band-stripe" points="0,512 1120,387 1120,399 0,524" fill="var(--green)"/>
    <polygon class="band-main" points="0,524 1120,399 1120,759 0,759" fill="url(#bandGrad)"/>
    <polygon class="band-booth" points="565,759 1120,693 1120,759" fill="var(--sky)"/>

    <polygon role="img" aria-label="Photo: smiling child care worker" points="617,145 833,88 837,378 622,396" fill="url(#photoPeople)" stroke="var(--green-light)" stroke-width="4" stroke-linejoin="round"/>
    <polygon role="img" aria-label="Photo: two smiling children outdoors" points="862,110 1066,61 1075,342 864,367" fill="url(#photoKids)" stroke="var(--sky)" stroke-width="4" stroke-linejoin="round"/>
    <polygon role="img" aria-label="Photo: fresh salad with tomatoes and peppers" points="623,424 838,403 842,639 627,696" fill="url(#photoProduce)" stroke="var(--green-light)" stroke-width="4" stroke-linejoin="round"/>
    <polygon role="img" aria-label="Photo: stacked disposable face masks" points="862,396 1076,371 1079,603 875,668" fill="url(#photoPpe)" stroke="var(--sky)" stroke-width="4" stroke-linejoin="round"/>
  </svg>

  <div class="brand"><span class="brand-square"></span><span class="brand-name">PantryWise Hub</span></div>

  <h1 class="headline">
    <span class="headline-lead">SAVE MONEY ON</span>
    <span class="headline-food">FOOD AND</span>
    <span class="headline-supplies">SUPPLIES</span>
  </h1>

  <div class="services-ribbon">Services that we provide</div>

  <ul class="services services-left">
    <li>Discounted food pricing</li>
    <li>Use of Registered Dietitian</li>
    <li>Free menu planning/design</li>
  </ul>
  <ul class="services services-right">
    <li>Huge selection of discounted<br>PPE and other necessary<br>supplies to run any child care center</li>
  </ul>

  <p class="cta">
    <span class="cta-request">Request Your <span class="cta-free">FREE Cost Analysis</span></span>
    <span class="cta-call">Call us at (800) 555-0199</span>
  </p>

  <p class="website">
    <svg width="18" height="18" viewBox="0 0 20 20" aria-hidden="true"><g fill="none" stroke="#fff" stroke-width="1.6"><circle cx="10" cy="10" r="8"/><ellipse cx="10" cy="10" rx="3.5" ry="8"/><line x1="2" y1="10" x2="18" y2="10"/></g></svg>
    www.pantrywisehub-example.com
  </p>
  <p class="booth">Join our booth #212</p>
</div>
</body>
</html>
```